skincare creams for tired moms

I need a package and a logo design for a skincare company based in California called Lumen Petal. I make day and night cream, under eye cream, and body lotion. The first product I plan to launch is an under eye cream. It does not have to be in these colors but I do teals, greens, black, and cobalt blue.

The package is going to either be in a box or a bag. Either way I go it will be like a gift box or bag. The design should make the person feel like they are getting something special and luxurious just for them.
Updates

I have small kids and it is really difficult to find a chunk of time to myself to update or review.

Need extra days to review

Target Market(s)

mainly first time moms. I am making an under eye cream that does not use retinol but is still powerful enough to get rid of bags and dark circles.

Industry/Entity Type

Cosmetics

Logo Text

The package and logo should incorporate the name Lumen Petal.

Font styles to use
Decorative
Script

Colors

Designer to choose colors to be used in the design.

Requirements
Nice to have
• maybe focus more on Petal instead of Lumen. Also incorporate plants or flowers
Should not have
• not a huge fan of pink

```html
<!DOCTYPE html>
<html lang="en">
<head>
<meta charset="utf-8">
<title>Lumen Petal — Under Eye Cream Packaging</title>
<link href="https://fonts.googleapis.com/css2?family=Playfair+Display:wght@700&family=Josefin+Sans:wght@400&display=swap" rel="stylesheet">
<style>
  :root {
    --backdrop: #f3e6e1;
    --paper: #fbf8f6;
    --leaf-green: #8fd3a8;
    --leaf-green-mid: #c4e9d1;
    --cobalt: #1b44be;
    --teal: #009494;
    --ink: #1c1c1c;
    --muted-ink: #6a6a6a;
  }
  * { box-sizing: border-box; margin: 0; padding: 0; }
  html, body {
    width: 1200px; height: 900px; overflow: hidden;
    background: var(--backdrop);
    font-family: "Josefin Sans", sans-serif;
  }
  .canvas { position: relative; width: 1200px; height: 900px; }

  .panel {
    position: absolute;
    background: var(--paper);
    box-shadow: 0 1px 2px rgba(0,0,0,0.06);
    overflow: hidden;
  }
  .ornament {
    position: absolute;
    border-radius: 50%;
    background: radial-gradient(circle at 50% 50%,
      var(--leaf-green) 0%,
      var(--leaf-green-mid) 45%,
      rgba(196,233,209,0.45) 70%,
      rgba(251,248,246,0) 100%);
  }

  /* tall carton */
  .carton-side-left { left: 110px; top: 130px; width: 200px; height: 620px; }
  .carton-front { left: 312px; top: 130px; width: 210px; height: 620px; }
  .carton-side-right { left: 524px; top: 130px; width: 200px; height: 620px; }

  .side-copy {
    position: absolute; right: 18px;
    font-size: 11px; line-height: 1.3; color: var(--ink);
    text-align: justify; text-align-last: right;
  }
  .side-copy.first { top: 488px; width: 80px; }
  .side-copy.second { top: 555px; width: 130px; }

  .wordmark {
    position: absolute; left: 0; right: 0;
    font-family: "Playfair Display", serif; font-weight: 700;
    color: var(--cobalt); text-align: center;
    text-transform: uppercase; line-height: 1;
  }
  .wordmark .name-main { display: block; letter-spacing: 0.14em; }
  .wordmark .name-sub { display: block; font-size: 7px; letter-spacing: 0.7em; margin-top: 5px; padding-left: 0.7em; }
  .carton-front .wordmark { top: 250px; font-size: 30px; }

  .product-name {
    position: absolute; left: 0; right: 0; bottom: 88px;
    text-align: center; font-size: 9px; letter-spacing: 0.6em;
    color: var(--teal); text-transform: uppercase;
  }
  .net-weight-band {
    position: absolute; left: 0; right: 0; bottom: 0; height: 62px;
    background: var(--teal);
  }
  .net-weight-band span {
    position: absolute; left: 12px; top: 14px;
    font-size: 7px; color: var(--paper); letter-spacing: 0.05em;
  }
  .directions {
    position: absolute; left: 18px; bottom: 40px; width: 110px;
    font-size: 8px; line-height: 1.6; color: var(--muted-ink);
  }

  /* small jar carton */
  .jar-top { left: 790px; top: 330px; width: 270px; height: 110px; background: var(--cobalt); }
  .jar-front { left: 790px; top: 442px; width: 270px; height: 250px; }
  .jar-side { left: 1062px; top: 442px; width: 110px; height: 250px; background: var(--teal); }
  .jar-front .wordmark { top: 105px; font-size: 28px; }
  .jar-front .net-weight {
    position: absolute; left: 14px; bottom: 14px;
    font-size: 13px; color: var(--ink);
  }
</style>
</head>
<body>
<main class="canvas">

  <section class="panel carton-side-left">
    <div class="ornament" style="left:-70px;top:20px;width:150px;height:150px" role="img" aria-label="Green line-art floral mandala ornament"></div>
    <div class="ornament" style="left:15px;top:190px;width:150px;height:150px" role="img" aria-label="Green line-art floral mandala ornament"></div>
    <div class="ornament" style="left:-70px;top:350px;width:150px;height:150px" role="img" aria-label="Green line-art floral mandala ornament"></div>
    <p class="side-copy first">Lorem ipsum dolor sit amet, consectetuer adipiscing elit, sed</p>
    <p class="side-copy second">diam nonummy nibh euismod tincidunt ut laoreet Lorem ipsum dolor sit amet, eet</p>
  </section>

  <section class="panel carton-front">
    <div class="ornament" style="left:-60px;top:20px;width:150px;height:150px" role="img" aria-label="Green line-art floral mandala ornament"></div>
    <div class="ornament" style="left:120px;top:20px;width:150px;height:150px" role="img" aria-label="Green line-art floral mandala ornament"></div>
    <div class="ornament" style="left:25px;top:190px;width:160px;height:160px" role="img" aria-label="Green line-art floral mandala ornament framing the name"></div>
    <div class="ornament" style="left:-60px;top:370px;width:150px;height:150px" role="img" aria-label="Green line-art floral mandala ornament"></div>
    <div class="ornament" style="left:120px;top:370px;width:150px;height:150px" role="img" aria-label="Green line-art floral mandala ornament"></div>
    <h1 class="wordmark"><span class="name-main">Lumen</span><span class="name-sub">Petal</span></h1>
    <p class="product-name">Under Eye Cream</p>
    <div class="net-weight-band"><span>0.5 OZ</span></div>
  </section>

  <section class="panel carton-side-right">
    <div class="ornament" style="left:-70px;top:20px;width:150px;height:150px" role="img" aria-label="Green line-art floral mandala ornament"></div>
    <div class="ornament" style="left:50px;top:150px;width:160px;height:160px" role="img" aria-label="Green line-art floral mandala ornament"></div>
    <div class="ornament" style="left:-60px;top:330px;width:150px;height:150px" role="img" aria-label="Green line-art floral mandala ornament"></div>
    <p class="directions">Directions: pat a small amount under eyes morning and night.</p>
  </section>

  <div class="panel jar-top"></div>
  <section class="panel jar-front">
    <div class="ornament" style="left:50px;top:20px;width:170px;height:170px" role="img" aria-label="Green line-art floral mandala ornament framing the name"></div>
    <h2 class="wordmark"><span class="name-main">Lumen</span><span class="name-sub">Petal</span></h2>
    <p class="net-weight">0.5 OZ</p>
  </section>
  <div class="panel jar-side"></div>

</main>
</body>
</html>
```